Urgent seeking Cover Design for event

An Outdoor Movie Event company in singapore is seeking for a Cover Design to be placed on Quorvent for an outdoor movie event at a location called Halvern Gardens.
Cover design size is 920px by 450px
We have provided images in this project for your side to come out with something suitable but not too complicated.
We urgently need the design which can be in PDF format for easy editing on our ends. We also need all readable and editable working files.

Target Market(s)

movie goers

Colors

Designer to choose colors to be used in the design.

Requirements
Must have
• Simple design to incorporate images provided if able to.
Nice to have
• Cover size to be 920px by 450px
Should not have
• Not be too messy

```html
<!DOCTYPE html>
<html lang="en">
<head>
<meta charset="utf-8">
<title>Outdoor Movie Night – Halvern Gardens</title>
<link rel="stylesheet" href="https://fonts.googleapis.com/css2?family=Jost:wght@300;400;600&display=swap">
<style>
  :root {
    --maroon: #5e0d14;
    --maroon-veil: rgba(120, 40, 55, 0.62);
    --white: #ffffff;
    --sky-top: #2f4f9a;
    --sky-mid: #7f95c8;
    --lawn: #2f5a2c;
    --lawn-dark: #1c3418;
    --plaza-gold: #c9a24a;
    --fountain: #7fc9cc;
  }
  * { margin: 0; padding: 0; box-sizing: border-box; }
  html, body { width: 1200px; height: 586px; overflow: hidden; background: var(--white); }
  .cover {
    position: relative;
    width: 1200px;
    height: 586px;
    overflow: hidden;
    font-family: "Jost", sans-serif;
    color: var(--white);
  }
  .event-photo {
    position: absolute;
    inset: 0;
    background:
      radial-gradient(ellipse 420px 260px at 1010px 300px, rgba(201,162,74,0.85), rgba(201,162,74,0) 70%),
      radial-gradient(ellipse 260px 120px at 900px 340px, rgba(127,201,204,0.7), rgba(127,201,204,0) 70%),
      linear-gradient(180deg, var(--sky-top) 0%, var(--sky-mid) 35%, var(--lawn) 62%, var(--lawn-dark) 100%);
  }
  .wave {
    position: absolute;
    inset: 0;
    width: 1200px;
    height: 586px;
  }
  .wave path { fill: var(--maroon); }
  .brand-box {
    position: absolute;
    left: 29px;
    top: 27px;
    width: 315px;
    height: 73px;
    background: var(--maroon);
    display: flex;
    align-items: center;
    justify-content: center;
  }
  .brand-name {
    font-family: "Jost", sans-serif;
    font-weight: 400;
    font-size: 34px;
    letter-spacing: 3px;
    color: var(--white);
  }
  .title-band {
    position: absolute;
    left: 260px;
    top: 153px;
    width: 685px;
    height: 104px;
    background: var(--maroon-veil);
  }
  .event-title {
    position: absolute;
    left: 314px;
    top: 176px;
    font-weight: 600;
    font-size: 50px;
    line-height: 56px;
    letter-spacing: 0.5px;
    white-space: nowrap;
  }
  .social-links {
    position: absolute;
    left: 35px;
    top: 515px;
    display: flex;
    gap: 12px;
  }
  .social-dot {
    width: 44px;
    height: 44px;
    border-radius: 50%;
    background: var(--white);
  }
  .footer-note {
    position: absolute;
    left: 231px;
    top: 515px;
    width: 520px;
    font-weight: 300;
    font-size: 17.5px;
    line-height: 22px;
  }
  .event-details {
    position: absolute;
    left: 790px;
    top: 401px;
    width: 372px;
    font-weight: 300;
    font-size: 18.5px;
    line-height: 22px;
    text-align: justify;
  }
</style>
</head>
<body>
  <main class="cover">
    <div class="event-photo" role="img" aria-label="Night-time outdoor movie screening on a lawn at Halvern Gardens with an inflatable screen, picnicking audience, and a lit plaza with fountains"></div>

    <svg class="wave" viewBox="0 0 1200 586" aria-hidden="true">
      <path d="M0,419 C70,468 150,504 250,501 C520,492 820,372 1200,340 L1200,586 L0,586 Z"/>
    </svg>

    <header class="brand-box">
      <span class="brand-name">LUMENVALE</span>
    </header>

    <div class="title-band"></div>
    <h1 class="event-title">LOREM IPSUM DOLOR SIT</h1>

    <nav class="social-links" aria-label="Social media">
      <span class="social-dot"></span>
      <span class="social-dot"></span>
      <span class="social-dot"></span>
    </nav>

    <p class="footer-note">Lorem ipsum dolor sit amet, consectetuer adipiscing elit, sed diam nonummy nibh euismod tincidunt ut laoreet dolore lore</p>

    <p class="event-details">Lorem ipsum dolor sit amet, consectetuer adipiscing elit, sed diam nonummy nibh euismod tincidunt ut laoreet dolore magna aliquam erat volutpat. Ut wisi enim ad minim veniam, quis nostrud exerci tation ullamcorper suscipit lobortis nisl ut aliquip ex ea commodo</p>
  </main>
</body>
</html>
```